Investment company seeks website design

TBW (Tallowbrook Wealth Partners) are an investment company that actively targets and acquires businesses and grows them after acquisition.

The website design needs to be professional and should communicate to key decision-makers inside the acquirable companies that TBW targets.

You will design the Homepage initially for the competition. If you win the competition, you will design the inner pages too.

More details are attached below.

Target Market(s)

Business owners and decision makers inside acquirable companies

Industry/Entity Type

Company Investment

Number of Pages Required

5+ page

Requirements
Must have
• High Attention to Detail. Following the Wireframes closely. Consistent colour and design choices
Should not have
• Anything cheap, too bright or untidy

```html
<!DOCTYPE html>
<html lang="en">
<head>
<meta charset="utf-8">
<title>Tallowbrook Wealth Partners</title>
<link href="https://fonts.googleapis.com/css2?family=Roboto:wght@400;500;700&display=swap" rel="stylesheet">
<style>
:root{
  --green:#75b443;
  --green-dark:#5f9a34;
  --navy:#223a6c;
  --navy-deep:#1b2f59;
  --ink:#151515;
  --text:#2b2b2b;
  --grey-bg:#f3f4f6;
  --footer:#000;
  --white:#fff;
}
*{margin:0;padding:0;box-sizing:border-box}
html,body{width:1200px;height:5046px;overflow:hidden}
body{font-family:"Roboto",sans-serif;color:var(--text);background:var(--white);position:relative}
section,header,footer{position:absolute;left:0;width:1200px}
.abs{position:absolute}
.center-x{left:0;width:1200px;text-align:center}
.btn{position:absolute;display:flex;align-items:center;justify-content:center;font-weight:500;font-size:15px;border-radius:3px;color:var(--white);background:var(--green)}
.hex{position:absolute;clip-path:polygon(50% 0,100% 25%,100% 75%,50% 100%,0 75%,0 25%);display:flex;align-items:center;justify-content:center}

/* header */
.site-header{top:0;height:98px;background:var(--white)}
.brand{left:98px;top:24px;display:flex;align-items:center;gap:12px}
.brand-mark{width:44px;height:44px;background:var(--navy)}
.brand-name{font-size:24px;font-weight:500;color:var(--navy);letter-spacing:1px}
.header-email{right:98px;top:14px;font-size:15px;color:var(--ink);display:flex;align-items:center;gap:8px}
.main-nav{right:98px;top:54px;display:flex;gap:44px;font-size:16px;color:var(--ink)}

/* hero */
.hero{top:98px;height:601px}
.hero-left{left:0;top:0;width:600px;height:601px;background:linear-gradient(135deg,#8cc45e,#6aa83c)}
.hero-right{left:600px;top:0;width:600px;height:601px;background:linear-gradient(135deg,#2a4477,#1f3666)}
.hero-title{font-size:53px;font-weight:700;color:var(--white);text-align:center;line-height:66px}
.hero-title.left{left:105px;top:190px;width:400px}
.hero-title.right{left:690px;top:192px;width:410px}
.hero-name{left:530px;top:218px;width:140px;text-align:center;font-size:40px;font-weight:700;color:var(--white)}
.hero .btn{left:519px;top:368px;width:160px;height:59px;background:var(--white);color:var(--navy);font-size:19px;font-weight:700;border-radius:4px}

/* thrive */
.thrive{top:699px;height:726px}
.thrive h2{left:98px;top:110px;font-size:33px;font-weight:700;color:var(--ink);line-height:40px}
.thrive-copy{left:98px;top:210px;width:440px;font-size:14.5px;line-height:31px}
.services-title{left:98px;top:348px;font-size:20px;font-weight:500;color:var(--navy)}
.services{left:98px;top:389px;list-style:none;font-size:14.5px;line-height:31px}
.thrive .btn{left:98px;top:572px;width:184px;height:45px}
.thrive-accent{left:959px;top:127px;width:151px;height:145px;background:var(--navy)}
.thrive-frame{left:615px;top:147px;width:471px;height:462px;border:3px solid var(--green)}
.thrive-photo{left:632px;top:137px;width:466px;height:454px;background:linear-gradient(120deg,#d5dde2,#8a9aa6 55%,#4b6175)}

/* qualities */
.qualities{top:1425px;height:820px;background:linear-gradient(160deg,#2d4a82,#1f3766 60%,#223a6c)}
.qualities h2{top:86px;font-size:31px;font-weight:700;color:var(--white)}
.q-box{position:absolute;width:292px;height:190px;border:2px solid var(--white);border-radius:6px;text-align:center;color:var(--white)}
.q-box h3{margin-top:64px;font-size:21px;font-weight:700}
.q-box ul{list-style:none;margin-top:10px;font-size:12.5px;line-height:25.5px}
.q-icon{width:88px;height:96px;background:var(--green)}
.q-core{left:480px;top:307px;width:241px;height:241px;border:3px solid var(--white);border-radius:50%;display:flex;align-items:center;justify-content:center;color:var(--white);font-size:42px;font-weight:500;letter-spacing:2px}

/* explore */
.explore{top:2245px;height:384px}
.explore h2{top:92px;font-size:31px;font-weight:700;color:var(--ink)}
.explore p{left:170px;width:860px;top:150px;text-align:center;font-size:16.5px;line-height:31px}
.explore .btn{left:513px;top:241px;width:176px;height:45px}

/* transform */
.transform{top:2629px;height:736px;background:linear-gradient(180deg,#7cba4b,#6aab3c)}
.transform h2{top:74px;font-size:31px;font-weight:700;color:var(--white)}
.t-card{position:absolute;top:163px;width:317px;border-radius:8px;overflow:hidden;background:var(--white);box-shadow:0 4px 8px rgba(0,0,0,.2)}
.t-card .t-photo{height:244px}
.t-card .t-label{height:77px;display:flex;align-items:center;justify-content:center;font-size:17px;font-weight:500;color:var(--ink)}
.t-card.featured{background:var(--navy);height:465px;box-shadow:none}
.t-panel{position:absolute;left:12px;top:244px;width:292px;height:206px;background:var(--white);border-radius:0 0 6px 6px;text-align:center}
.t-panel h3{margin-top:22px;font-size:17px;font-weight:700;color:var(--navy)}
.t-panel p{margin-top:12px;font-size:14.5px;line-height:31px;color:var(--ink)}

/* news */
.news{top:3365px;height:711px}
.news h2{top:96px;font-size:31px;font-weight:700;color:var(--ink)}
.n-card{position:absolute;top:170px;width:317px;height:419px}
.n-photo{position:absolute;left:0;top:0;width:317px;height:419px}
.n-card svg{position:absolute;left:0;top:0}
.n-body{position:absolute;left:20px;top:235px;width:270px;color:var(--white)}
.n-date{font-size:14.5px;color:var(--green)}
.n-title{margin-top:8px;font-size:17px;font-weight:700}
.n-text{margin-top:8px;font-size:13.5px;line-height:31px}

/* group */
.group{top:4076px;height:524px;background:var(--grey-bg)}
.group h2{top:84px;font-size:33px;font-weight:700;color:var(--ink)}
.group p{top:144px;font-size:14.5px;line-height:30px;color:var(--ink)}
.pillar{position:absolute;top:238px;width:200px;text-align:center}
.pillar .hex{position:relative;margin:0 auto;width:121px;height:137px}
.pillar span{display:block;margin-top:28px;font-size:21px;font-weight:500;color:var(--ink);letter-spacing:.5px}
.hex.navy{background:var(--navy)}
.hex.green{background:var(--green)}

/* footer */
.site-footer{top:4600px;height:446px;background:var(--footer);color:var(--white)}
.f-col h4{font-size:24px;font-weight:700;margin-bottom:16px}
.f-links{list-style:none;font-size:14.5px;line-height:31px}
.f-rule{position:absolute;top:88px;width:2px;height:176px;background:var(--white)}
.f-item{display:flex;align-items:flex-start;gap:16px;font-size:14.5px;line-height:31px}
.f-dot{width:35px;height:35px;border-radius:50%;background:var(--green);flex:none;display:flex;align-items:center;justify-content:center}
.f-bottom-rule{left:98px;top:368px;width:1004px;height:1px;background:#8a8a8a}
.f-copy{left:98px;top:396px;font-size:14.5px}
.f-legal{right:98px;top:396px;display:flex;gap:28px;font-size:14.5px}
</style>
</head>
<body>

<header class="site-header">
  <div class="abs brand"><div class="brand-mark"></div><div class="brand-name">TALLOWBROOK</div></div>
  <div class="abs header-email">
    <svg width="20" height="15" viewBox="0 0 20 15"><rect width="20" height="15" rx="2" fill="#75b443"/><path d="M2 3l8 6 8-6" stroke="#fff" stroke-width="1.8" fill="none"/></svg>
    info@tallowbrook.com
  </div>
  <nav class="abs main-nav"><span>Our Approach</span><span>Investment Criteria</span><span>About Us</span><span>Contact Us</span></nav>
</header>

<section class="hero">
  <div class="abs hero-left" role="img" aria-label="Businesswoman holding a tablet in an office, green tint"></div>
  <div class="abs hero-right" role="img" aria-label="Team meeting around a table, navy tint"></div>
  <h1 class="abs hero-title left">The Best Exit For You</h1>
  <div class="abs hero-name">TBW</div>
  <h1 class="abs hero-title right">The Best Future For Your Business</h1>
  <a class="btn">Discover TBW</a>
</section>

<section class="thrive">
  <h2 class="abs">We Will Make Your Business<br>Thrive</h2>
  <p class="abs thrive-copy">TBW is committed to helping businesses achieve significant growth. Under our stewardship, companies have the benefit of an experienced team expert in operations and financing to ensure that every company achieves their full potential.</p>
  <h3 class="abs services-title">Our services include:</h3>
  <ul class="abs services">
    <li>• Crafting long-term growth</li>
    <li>• Streamlining operations for maximum efficiency</li>
    <li>• Providing expert advice to improve management decisions</li>
    <li>• Optimising financial structures for expansion</li>
    <li>• Facilitating strategic mergers and acquisitions</li>
  </ul>
  <a class="btn">Unlock Your Potential</a>
  <div class="abs thrive-accent"></div>
  <div class="abs thrive-frame"></div>
  <div class="abs thrive-photo" role="img" aria-label="Two businessmen shaking hands"></div>
</section>

<section class="qualities" role="region" aria-label="Qualities and capabilities">
  <h2 class="abs center-x">Our Qualities &amp; Capabilities</h2>

  <div class="q-box" style="left:123px;top:211px">
    <h3>Driving Value</h3>
    <ul><li>• Comprehensive long-term plan</li><li>• Ownership of company performance</li><li>• Vast experience in driving transformation</li></ul>
  </div>
  <div class="hex q-icon" style="left:225px;top:165px">
    <svg width="48" height="40" viewBox="0 0 48 40" fill="none" stroke="#fff" stroke-width="2"><path d="M4 36h40"/><rect x="8" y="24" width="6" height="12"/><rect x="18" y="18" width="6" height="18"/><rect x="28" y="12" width="6" height="24"/><path d="M6 18l12-8 8 4 14-10M34 4h6v6"/></svg>
  </div>

  <div class="q-box" style="left:777px;top:211px">
    <h3>Integrated Team</h3>
    <ul><li>• Partnership Culture</li><li>• Consistent senior team</li><li>• Detailed industry and operating</li></ul>
  </div>
  <div class="hex q-icon" style="left:879px;top:165px">
    <svg width="46" height="44" viewBox="0 0 46 44" fill="none" stroke="#fff" stroke-width="2"><circle cx="13" cy="12" r="8"/><circle cx="33" cy="12" r="8"/><circle cx="13" cy="32" r="8"/><circle cx="33" cy="32" r="8"/></svg>
  </div>

  <div class="q-box" style="left:123px;top:503px">
    <h3>Partnership Management</h3>
    <ul><li>• Strong, trust-based relationships</li><li>• Significant commitment of time</li><li>• Ability to take interim roles if needed</li></ul>
  </div>
  <div class="hex q-icon" style="left:225px;top:457px">
    <svg width="46" height="40" viewBox="0 0 46 40" fill="none" stroke="#fff" stroke-width="2"><path d="M3 14l10-8 10 6 10-6 10 8M8 18l10 12a3 3 0 004 0l16-14"/><circle cx="23" cy="22" r="14"/></svg>
  </div>

  <div class="q-box" style="left:777px;top:503px">
    <h3>Accelerated Execution</h3>
    <ul><li>• Relentless focus on priorities</li><li>• Drive through to results</li><li>• Committed to continuous development</li></ul>
  </div>
  <div class="hex q-icon" style="left:879px;top:457px">
    <svg width="46" height="44" viewBox="0 0 46 44" fill="none" stroke="#fff" stroke-width="2"><circle cx="16" cy="16" r="9"/><circle cx="16" cy="16" r="3"/><circle cx="32" cy="30" r="7"/><circle cx="32" cy="30" r="2"/><path d="M16 3v4M16 25v4M3 16h4M25 16h4"/></svg>
  </div>

  <div class="abs q-core">TBW</div>
</section>

<section class="explore">
  <h2 class="abs center-x">Explore Your Next Move</h2>
  <p class="abs">If you are looking for a change, then TBW can help you map out a smooth transition, and give you the confidence that your company is in safe hands.</p>
  <a class="btn">Discuss with TBW</a>
</section>

<section class="transform">
  <h2 class="abs center-x">How TBW Will Transform Your Company</h2>
  <div class="t-card" style="left:98px">
    <div class="t-photo" role="img" aria-label="Businessman touching rising growth chart" style="background:linear-gradient(135deg,#2b4a7a,#152a4f)"></div>
    <div class="t-label">Discover Growth Opportunities</div>
  </div>
  <div class="t-card featured" style="left:442px">
    <div class="t-photo" role="img" aria-label="Hand stacking wooden blocks onto a target" style="background:linear-gradient(160deg,#7a6a5c,#c8a27a 60%,#e8ddd0)"></div>
    <div class="t-panel">
      <h3>Craft Strategic Solutions</h3>
      <p>Develop precise,<br>results-driven strategies to<br>drive your company<br>forward</p>
    </div>
  </div>
  <div class="t-card" style="left:785px">
    <div class="t-photo" role="img" aria-label="Smiling businesswoman in a city at sunset" style="background:linear-gradient(135deg,#e9c98a,#a6b2b8 55%,#5e6d78)"></div>
    <div class="t-label">Drive Future Success</div>
  </div>
</section>

<section class="news">
  <h2 class="abs center-x">TBW News &amp; Insights</h2>

  <div class="n-card" style="left:98px">
    <div class="n-photo" role="img" aria-label="Businessman climbing stairs towards light" style="background:linear-gradient(180deg,#d9a56a,#5d6b7c 60%,#2c3848)"></div>
    <svg width="317" height="419" viewBox="0 0 317 419"><polygon points="1.5,170 292,240 292,417.5 1.5,417.5" fill="#223a6c" stroke="#75b443" stroke-width="3"/><line x1="292" y1="240" x2="317" y2="246" stroke="#75b443" stroke-width="3"/></svg>
    <div class="n-body"><div class="n-date">Mar 12 2022</div><div class="n-title">Lorem ipsum dolor amet</div><div class="n-text">Sed ut perspiciatis unde omnis iste natus error sit voluptatem accusantium doloremque laudantium, totam aperiam</div></div>
  </div>

  <div class="n-card" style="left:442px">
    <div class="n-photo" role="img" aria-label="Presenter speaking at a whiteboard" style="background:linear-gradient(180deg,#b46a52,#d8d2c8 50%,#7d7a72)"></div>
    <svg width="317" height="419" viewBox="0 0 317 419"><polygon points="1.5,170 292,240 292,417.5 1.5,417.5" fill="#223a6c" stroke="#75b443" stroke-width="3"/><line x1="292" y1="240" x2="317" y2="246" stroke="#75b443" stroke-width="3"/></svg>
    <div class="n-body"><div class="n-date">Mar 12 2022</div><div class="n-title">Lorem ipsum dolor amet</div><div class="n-text">Sed ut perspiciatis unde omnis iste natus error sit voluptatem accusantium doloremque laudantium, totam aperiam</div></div>
  </div>

  <div class="n-card" style="left:785px">
    <div class="n-photo" role="img" aria-label="Engineers discussing plans in a factory" style="background:linear-gradient(180deg,#a7b4bf,#5a6a78 55%,#39434d)"></div>
    <svg width="317" height="419" viewBox="0 0 317 419"><polygon points="1.5,170 292,240 292,417.5 1.5,417.5" fill="#223a6c" stroke="#75b443" stroke-width="3"/><line x1="292" y1="240" x2="317" y2="246" stroke="#75b443" stroke-width="3"/></svg>
    <div class="n-body"><div class="n-date">Mar 12 2022</div><div class="n-title">Lorem ipsum dolor amet</div><div class="n-text">Sed ut perspiciatis unde omnis iste natus error sit voluptatem accusantium doloremque laudantium, totam aperiam</div></div>
  </div>
</section>

<section class="group">
  <h2 class="abs center-x">Tallowbrook Wealth Partners</h2>
  <p class="abs center-x">Providing Balance and Growth<br>to Your Business</p>
  <div class="pillar" style="left:102px">
    <div class="hex navy"><svg width="54" height="50" viewBox="0 0 54 50" fill="none" stroke="#fff" stroke-width="2"><path d="M4 46h46"/><rect x="10" y="30" width="8" height="16"/><rect x="23" y="20" width="8" height="26"/><rect x="36" y="10" width="8" height="36"/><path d="M8 20l14-12 10 6 14-10"/></svg></div>
    <span>FINANCE</span>
  </div>
  <div class="pillar" style="left:352px">
    <div class="hex green"><svg width="56" height="44" viewBox="0 0 56 44" fill="none" stroke="#fff" stroke-width="2"><path d="M2 14l12-8 14 8 14-8 12 8M8 20l14 16a4 4 0 006 0l20-18M18 26l6 6M24 22l6 6"/></svg></div>
    <span>PARTNERSHIPS</span>
  </div>
  <div class="pillar" style="left:603px">
    <div class="hex navy"><svg width="54" height="50" viewBox="0 0 54 50" fill="none" stroke="#fff" stroke-width="2"><rect x="4" y="6" width="40" height="30"/><path d="M10 28l8-8 6 5 10-11"/><circle cx="38" cy="34" r="8"/><path d="M44 40l6 6"/></svg></div>
    <span>STRATEGY</span>
  </div>
  <div class="pillar" style="left:853px">
    <div class="hex green"><svg width="54" height="50" viewBox="0 0 54 50" fill="none" stroke="#fff" stroke-width="2"><circle cx="27" cy="16" r="10"/><circle cx="27" cy="16" r="4"/><path d="M27 2v4M27 26v4M13 16h4M37 16h4M8 46v-6a6 6 0 0112 0v6M34 46v-6a6 6 0 0112 0v6M21 46v-4a6 6 0 0112 0v4"/></svg></div>
    <span>OPERATIONS</span>
  </div>
</section>

<footer class="site-footer">
  <div class="abs f-col" style="left:98px;top:90px">
    <h4>Quick Links</h4>
    <ul class="f-links"><li>Our Approach</li><li>Investment Criteria</li><li>About Us</li><li>Contact Us</li></ul>
  </div>
  <div class="f-rule" style="left:333px"></div>
  <div class="abs f-col" style="left:423px;top:90px">
    <h4>Our Team</h4>
    <div class="f-item"><span class="f-dot"><svg width="16" height="12" viewBox="0 0 16 12"><rect width="16" height="12" rx="1" fill="#fff"/><path d="M1 2l7 5 7-5" stroke="#75b443" stroke-width="1.5" fill="none"/></svg></span><span>info@tallowbrook.com</span></div>
    <div class="f-item" style="margin-top:28px"><span class="f-dot"><svg width="16" height="16" viewBox="0 0 16 16"><path d="M3 1l3 3-2 2a9 9 0 006 6l2-2 3 3-2 2C7 15 1 9 1 3z" fill="#fff"/></svg></span><span>+44 (0) 7700 900123</span></div>
  </div>
  <div class="f-rule" style="left:728px"></div>
  <div class="abs f-col" style="left:808px;top:90px">
    <h4>Address</h4>
    <div class="f-item"><span class="f-dot"><svg width="16" height="12" viewBox="0 0 16 12"><rect width="16" height="12" rx="1" fill="#fff"/><path d="M1 2l7 5 7-5" stroke="#75b443" stroke-width="1.5" fill="none"/></svg></span><span>Tallowbrook Wealth Partners Ltd.<br>Harbourline Business Centre Kingsway<br>St. Michael<br>Barbados</span></div>
  </div>
  <div class="abs f-bottom-rule"></div>
  <div class="abs f-copy">(c) Tallowbrook Wealth Partners</div>
  <div class="abs f-legal"><span>Sitemap</span><span>Terms of Use</span><span>Privacy Policy</span><span>Contact Us</span></div>
</footer>

</body>
</html>
```